Cobalto Grande

I want a glossy card on both sides. We sell underwater LED lights for water craft

we sell custom audio enclosures for automobile, boats and atv's.

view our websites for any other pictures you may think are better suited.

Industry/Entity Type

Audio

Contact Information for Business Card

Email address: CobaltoGrande@mailvista.example
Website: www.hullglowtap.example
underwater LED lighting for watercraft
boat drain plug lights
phone number: 555-271-0648

other side of card:
email address the same
website: www.versatilesoundshells.example
speaker enclosures, auto, boat and atv
same phone number

```html
<!DOCTYPE html>
<html lang="en">
<head>
<meta charset="utf-8">
<title>Cobalto Grande — Business Card</title>
<link rel="stylesheet" href="https://fonts.googleapis.com/css2?family=Great+Vibes&family=Arimo:wght@700&display=swap">
<style>
  :root {
    --page-bg: #8c8c8c;
    --card-black: #050505;
    --night-water: #111312;
    --glow-green: #6fd13a;
    --glow-deep: #1f5a14;
    --band-grey: rgba(150, 150, 150, 0.45);
    --text-white: #ffffff;
    --title-glow: #8cff5a;
  }
  * { margin: 0; padding: 0; box-sizing: border-box; }
  html, body {
    width: 1200px;
    height: 1000px;
    overflow: hidden;
    background: var(--page-bg);
  }
  .business-card {
    position: absolute;
    left: 150px;
    top: 230px;
    width: 900px;
    height: 540px;
    background: var(--card-black);
    overflow: hidden;
  }
  .hero-photo {
    position: absolute;
    inset: 0;
    width: 100%;
    height: 100%;
  }
  .contact-band {
    position: absolute;
    left: 0;
    right: 0;
    top: 300px;
    height: 170px;
    background: var(--band-grey);
  }
  .lower-stripe {
    position: absolute;
    left: 0;
    right: 0;
    top: 470px;
    bottom: 0;
    background: rgba(0, 0, 0, 0.55);
  }
  .brand-title {
    position: absolute;
    right: 60px;
    top: 150px;
    font-family: "Great Vibes", cursive;
    font-size: 64px;
    font-weight: 400;
    color: var(--text-white);
    text-shadow: 0 0 6px var(--title-glow), 0 0 14px var(--glow-green);
    white-space: nowrap;
  }
  .contact-list {
    position: absolute;
    left: 450px;
    top: 320px;
    list-style: none;
    font-family: "Arimo", Arial, sans-serif;
    font-weight: 700;
    font-size: 23px;
    line-height: 31px;
    color: var(--text-white);
    text-shadow: 0 0 2px #000, 1px 1px 1px #000;
    white-space: nowrap;
  }
  .contact-list .web { padding-left: 14px; }
  .contact-list .phone { padding-left: 48px; }
</style>
</head>
<body>
  <section class="business-card">
    <svg class="hero-photo" viewBox="0 0 900 540" role="img" aria-label="Photo of two center-console boats at night on dark water, lit by green underwater LED lights">
      <defs>
        <radialGradient id="glowFront" cx="0.42" cy="0.72" r="0.35">
          <stop offset="0" stop-color="var(--glow-green)"/>
          <stop offset="0.5" stop-color="var(--glow-deep)"/>
          <stop offset="1" stop-color="var(--night-water)" stop-opacity="0"/>
        </radialGradient>
        <radialGradient id="glowBack" cx="0.55" cy="0.42" r="0.25">
          <stop offset="0" stop-color="var(--glow-green)" stop-opacity="0.85"/>
          <stop offset="1" stop-color="var(--night-water)" stop-opacity="0"/>
        </radialGradient>
      </defs>
      <rect width="900" height="540" fill="var(--night-water)"/>
      <rect width="900" height="540" fill="url(#glowBack)"/>
      <rect width="900" height="540" fill="url(#glowFront)"/>
    </svg>
    <div class="contact-band"></div>
    <div class="lower-stripe"></div>
    <h1 class="brand-title">Cobalto Grande</h1>
    <ul class="contact-list">
      <li class="email">CobaltoGrande@mailvista.example</li>
      <li class="web">www.hullglowtap.example</li>
      <li class="phone">555-271-0648</li>
    </ul>
  </section>
</body>
</html>
```